Marketing Postcard Design for a Medical Supply Company

We are sending a marketing postcard to healthcare facilities within our state. We are in need of a design for a 6"x9" postcard, front and back with our logo, website www.curaloft.shop, phone number 808-413-2759, and 12 products. The products are face shields, nitrile gloves, vinyl gloves, isolation gowns, gallon hand sanitizer, black KN95's, white KN95's, 4320 R77, 4310 R77, biohazard bags, Purivane wipes, and Kol spray. All of these items can be found on our website at curaloft.shop. Please include a promo code, 10OFF for 10% Off. The design should be clean, professional, and appeal to a healthcare or medical audience.

```html
<!DOCTYPE html>
<html lang="en">
<head>
<meta charset="utf-8">
<title>Curaloft Medical Supply – Postcard</title>
<link href="https://fonts.googleapis.com/css2?family=Montserrat:wght@400;500;600;700;800&display=swap" rel="stylesheet">
<style>
  :root{
    --green:#0b9444;
    --green-dark:#0a5c2c;
    --ink:#2a2a2a;
    --grey:#6b6b6b;
    --card-top:#f4f5f7;
    --card-bottom:#dfe1e5;
    --line:#8a8a8a;
  }
  *{box-sizing:border-box;margin:0;padding:0}
  html,body{width:1200px;height:1200px;overflow:hidden;background:#fff;font-family:"Montserrat",sans-serif;color:var(--ink)}
  .canvas{position:relative;width:1200px;height:1200px}

  .brand{position:absolute;text-align:center;color:var(--green);font-family:"Montserrat",sans-serif;font-weight:800;line-height:1}
  .brand .dot{display:block;margin:0 auto;border-radius:50%;background:var(--green)}
  .brand-main{left:450px;top:72px;width:306px}
  .brand-main .dot{width:56px;height:56px;margin-bottom:22px}
  .brand-main .name{font-size:38px;letter-spacing:0}
  .brand-main .sub{font-size:12.5px;letter-spacing:4px;margin-top:6px}

  .card{position:absolute;top:277px;width:520px;height:779px;overflow:hidden;
    background:linear-gradient(160deg,var(--card-top) 0%,#eceef1 45%,var(--card-bottom) 100%);
    box-shadow:0 8px 18px rgba(0,0,0,.22)}
  .card-front{left:53px}
  .card-back{left:634px}
  .card .brand .dot{width:28px;height:28px;margin-bottom:8px}
  .card .brand .name{font-size:17px}
  .card .brand .sub{font-size:6.5px;letter-spacing:1.6px;margin-top:3px}

  .headline{position:absolute;left:26px;top:29px;font-size:34px;font-weight:800;color:var(--green);letter-spacing:.5px;line-height:1}
  .subline{position:absolute;left:26px;top:64px;font-size:14px;font-weight:400;color:#555;letter-spacing:.2px}
  .front-brand{left:406px;top:27px;width:90px}
  .intro{position:absolute;left:26px;top:120px;width:300px;font-size:12.5px;line-height:14px;color:#333}
  .intro strong{color:var(--green);font-weight:700}
  .shop-btn{position:absolute;left:26px;top:168px;width:109px;height:32px;border-radius:16px;background:var(--green);
    color:#fff;font-size:11px;font-weight:700;display:flex;align-items:center;justify-content:center;letter-spacing:.3px;
    box-shadow:0 2px 3px rgba(0,0,0,.25)}
  .collections{position:absolute;left:25px;top:245px;font-size:24px;font-weight:800;color:var(--green);letter-spacing:.3px}
  .promo-banner{position:absolute;left:340px;top:223px;width:126px;height:40px}
  .promo-circle{position:absolute;left:272px;top:203px;width:78px;height:78px;border-radius:50%;background:var(--green);
    color:#fff;text-align:center;display:flex;flex-direction:column;justify-content:center;font-weight:700;line-height:1.05}
  .promo-circle .lbl{font-size:13px}
  .promo-circle .code{font-size:12.5px;margin-top:3px}
  .promo-off{position:absolute;left:362px;top:229px;font-size:21px;font-weight:700;color:#fff}

  .product{position:absolute;width:120px;text-align:center}
  .product .photo{width:94px;height:94px;margin:0 auto;border-radius:50%;border:4px solid var(--green);background:#fff;overflow:hidden}
  .product .photo span{display:block;width:100%;height:100%}
  .product .label{margin-top:12px;font-size:12.5px;line-height:12.5px;color:#222}

  .footer-band{position:absolute;left:0;top:728px;width:520px;height:34px;background:var(--green);color:#fff}
  .footer-phone{position:absolute;left:26px;top:3px;display:flex;align-items:center;gap:8px;font-size:23px;font-weight:700}
  .footer-web{position:absolute;right:35px;top:8px;font-size:14px;font-weight:400}
  .footer-web b{font-weight:700}

  .back-brand{left:50px;top:32px;width:82px}
  .stamp{position:absolute;left:388px;top:23px;width:94px;height:86px;border:1px solid #444}
  .why{position:absolute;left:0;top:128px;width:520px;text-align:center;font-size:36px;font-weight:800;color:var(--green);letter-spacing:.5px}
  .para{position:absolute;left:12px;width:496px;text-align:center;font-size:14px;line-height:19.3px;color:#333}
  .para b{font-weight:700}
  .para-1{top:181px}
  .para-2{top:277px}
  .notice{position:absolute;left:37px;top:370px;width:445px;height:29px;background:var(--green-dark);color:#fff;
    font-size:16px;font-weight:700;display:flex;align-items:center;justify-content:center;letter-spacing:.3px}
  .ask{position:absolute;left:0;top:410px;width:520px;text-align:center;font-size:16.5px;line-height:17px;color:#8a8a8a}
  .email{position:absolute;left:0;top:452px;width:520px;text-align:center;font-size:22px;font-weight:500;color:var(--green-dark)}
  .call{position:absolute;left:0;top:480px;width:520px;text-align:center;font-size:29px;font-weight:700;color:var(--green)}
  .write-line{position:absolute;left:52px;width:416px;height:1px;background:var(--line)}
</style>
</head>
<body>
<main class="canvas">

  <div class="brand brand-main">
    <span class="dot"></span>
    <div class="name">CURALOFT</div>
    <div class="sub">MEDICAL SUPPLY</div>
  </div>

  <section class="card card-front">
    <h1 class="headline">YOUR ONE</h1>
    <p class="subline">STOP SHOPFOR ALL OF YOUR SUPPLIES</p>

    <div class="brand front-brand">
      <span class="dot"></span>
      <div class="name">CURALOFT</div>
      <div class="sub">MEDICAL SUPPLY</div>
    </div>

    <p class="intro"><strong>Health</strong> and safety supplies delivered to your business or the comfort of your own home</p>
    <div class="shop-btn">SHOP NOW</div>

    <h2 class="collections">COLLECTIONS</h2>
    <svg class="promo-banner" viewBox="0 0 126 40" aria-hidden="true">
      <polygon points="6,4 110,0 106,10 0,14" fill="var(--green)"/>
      <polygon points="0,6 126,6 116,40 0,40" fill="var(--green-dark)"/>
    </svg>
    <div class="promo-circle"><span class="lbl">Promo<br>Code:</span><span class="code">10OFF</span></div>
    <div class="promo-off">10% Off</div>

    <div class="product" style="left:16px;top:303px"><div class="photo"><span role="img" aria-label="Teal face shield mask" style="background:radial-gradient(circle,#2bb3b0,#e9f5f5 75%)"></span></div><div class="label">Face shields</div></div>
    <div class="product" style="left:134px;top:303px"><div class="photo"><span role="img" aria-label="Boxes of nitrile gloves" style="background:radial-gradient(circle,#5b6a9a,#f2f3f7 72%)"></span></div><div class="label">Nitrile gloves</div></div>
    <div class="product" style="left:258px;top:303px"><div class="photo"><span role="img" aria-label="Stacked boxes of vinyl gloves" style="background:radial-gradient(circle,#d6dde2,#fbfbfb 75%)"></span></div><div class="label">Vinyl gloves</div></div>
    <div class="product" style="left:381px;top:303px"><div class="photo"><span role="img" aria-label="Blue isolation gown" style="background:radial-gradient(ellipse at 50% 60%,#3d6fb5,#f4f6fa 70%)"></span></div><div class="label">Isolation gowns</div></div>

    <div class="product" style="left:16px;top:438px"><div class="photo"><span role="img" aria-label="Gallon bucket of hand sanitizer" style="background:radial-gradient(circle,#cfcfcf,#f6f6f6 75%)"></span></div><div class="label">Gallon hand<br>sanitizer</div></div>
    <div class="product" style="left:134px;top:438px"><div class="photo"><span role="img" aria-label="Black KN95 mask" style="background:radial-gradient(circle,#1a1a1a,#f4f4f4 65%)"></span></div><div class="label">Black KN95's</div></div>
    <div class="product" style="left:258px;top:438px"><div class="photo"><span role="img" aria-label="White KN95 mask" style="background:radial-gradient(circle,#e2e2e2,#fdfdfd 75%)"></span></div><div class="label">White KN95's</div></div>
    <div class="product" style="left:381px;top:438px"><div class="photo"><span role="img" aria-label="White folding respirator with red straps" style="background:radial-gradient(circle,#d8d8d8,#f6eeee 75%)"></span></div><div class="label">4320 R77</div></div>

    <div class="product" style="left:16px;top:584px"><div class="photo"><span role="img" aria-label="Light blue cup respirator" style="background:radial-gradient(circle,#43b5d9,#eef7fa 78%)"></span></div><div class="label">4310 R77</div></div>
    <div class="product" style="left:134px;top:584px"><div class="photo"><span role="img" aria-label="Roll of red biohazard bags" style="background:radial-gradient(circle,#d3202a,#f7eaea 72%)"></span></div><div class="label">Biohazard bags</div></div>
    <div class="product" style="left:258px;top:584px"><div class="photo"><span role="img" aria-label="Canister of disinfecting wipes" style="background:radial-gradient(circle,#c9ccd2,#fbfbfb 72%)"></span></div><div class="label">Purivane wipes</div></div>
    <div class="product" style="left:381px;top:584px"><div class="photo"><span role="img" aria-label="Gallon jug of disinfectant spray" style="background:radial-gradient(circle,#7fae58,#f2f5ee 72%)"></span></div><div class="label">Kol spray</div></div>

    <div class="footer-band">
      <div class="footer-phone">
        <svg width="22" height="22" viewBox="0 0 24 24" aria-hidden="true"><circle cx="12" cy="12" r="12" fill="#fff"/><path d="M8.2 6.2l1.9-.4 1.2 2.9-1.4 1.1c.7 1.5 1.8 2.6 3.3 3.3l1.1-1.4 2.9 1.2-.4 1.9c-.2.6-.7.9-1.3.9-4.3-.3-7.8-3.8-8.1-8.1 0-.6.3-1.1.8-1.4z" fill="var(--green)"/></svg>
        <span>808-413-2759</span>
      </div>
      <div class="footer-web">www.<b>curaloft</b>.shop</div>
    </div>
  </section>

  <section class="card card-back">
    <div class="brand back-brand">
      <span class="dot"></span>
      <div class="name">CURALOFT</div>
      <div class="sub">MEDICAL SUPPLY</div>
    </div>
    <div class="stamp"></div>

    <h2 class="why">WHY CHOOSE US?</h2>
    <p class="para para-1"><b>Curaloft's</b> sudden rise as a supplier of PPE, medical, and healthcare products during the COVID-19 pandemic in 2020 actually began 25 years earlier as part of Marian Keale's longtime commitment to helping people.</p>
    <p class="para para-2"><b>Curaloft</b> maintains a supply of all types of safety, health, and wellness items for businesses, schools, hospitals, government agencies, and households. If there's something specific that you need, we will find it for you.</p>

    <div class="notice">CAN'T FIND WHAT YOU ARE LOOKING FOR?</div>
    <p class="ask">If you need a different size or product than<br>what you see here email us at:</p>
    <p class="email">info@curaloft.shop</p>
    <p class="call">Call Us-808-413-2759</p>

    <div class="write-line" style="top:572px"></div>
    <div class="write-line" style="top:630px"></div>
    <div class="write-line" style="top:688px"></div>
    <div class="write-line" style="top:746px"></div>
  </section>

</main>
</body>
</html>
```